International Financial Organization needs a new Digital Workplace home page design

We need creative designs for the new Digital Workplace that will replace the current Intranet for an international organization based in Washington DC.

Organization Background: An organization of 189 countries, working to foster global monetary cooperation, secure financial stability, facilitate international trade, promote high employment and sustainable economic growth, and reduce poverty around the world.

Digital Workplace: The Digital workplace will be the central location that allows employees to do their work in productive, simple, and integrated manner.
Knowledge and Information are the lifeblood of our organization. Economists and experts conduct a lot of data-heavy research and produce a lot of reports and documents. The digital workplace will need to facilitate sharing of knowledge and collaboration among employees, and save them the hassle from going to multiple digital locations to do their work. Therefore the seamless integration of systems, and mobile-first design, is key.

Country Missions: A number of our economists travel on "missions" to countries all over the world on periodic basis to meet with country officials, present and discuss findings, and provide consultation. Before they go on missions, these economist do a lot of preparation and research about that country, and they collaborate in teams. When on mission (sometimes in areas that have very limited bandwidth connectivity) they need access to their documents, research, and resources and they need to collaborate with one another. Therefore mobility (velaphone, tabrik, laptop and desktops) and personalization are very important design criteria. When they are back from their mission they need to document reports and findings, and they will need to work on that through multiple systems.

Design Concept: We attach a concept of the digital workplace homepage (power point slides). The concept offers three views (the three tabs at the top: Enterprise View, Departmental View, and My View.)
The enterprise view is meant to be for all the users in the organization, and displays information that the org want to push to all employees. Not much of personalization is listed in this this view. We only provide the name of potential tiles there. Please be creative and think out of the box, we are open for ideas. The second view is the departmental view. It is meant to focus on the news, events, and information that the department want to share with me as an employee of that department. We only provide the name of potential tiles there. Please be creative and think out of the box, we are open for ideas.
Finally, “My View” is illustrated with sample tiles of what we envision to be used there. We provide two variations for our vision of the “My View”. The tiles that are listed there are not meant to be in that same exact location. Please feel free to change the groupings of these tiles as the page allows (We had to fit our design on 16:9 PPT slide so it’s a not a real page). Also, these tiles are not mean to be restrictive, please be creative and suggest other tiles as you’d envision a modern Digital Workplace. We are open for ideas!

Deliverables: we expect to see at least one creative design per each of these 3 views of the home page for desktop view, and the equivalent in mobile view. In addition we expect any other views/variations that your creativity inspires.

Preferred color pallet: blue, green, orange, and all their gradients. Also open for other colors as your creativity inspires for an established, very mature, and well-respected, international financial organization.

Thank you!

```html
<!DOCTYPE html>
<html lang="en">
<head>
<meta charset="utf-8">
<title>Corehub – My View</title>
<link href="https://fonts.googleapis.com/css2?family=Rubik:wght@400;500;700&display=swap" rel="stylesheet">
<style>
:root{
  --blue:#1c9ce0;
  --blue-dark:#0a5fb4;
  --blue-light:#19b4ef;
  --green:#0ea04b;
  --orange:#f7941d;
  --ink:#1d1d1d;
  --text:#333;
  --muted:#888;
  --line:#ececec;
  --row:#f6f6f6;
  --avatar:#b9a999;
}
*{box-sizing:border-box;margin:0;padding:0}
html,body{width:1103px;height:1200px;overflow:hidden;background:#fff}
body{font-family:"Rubik",Arial,sans-serif;color:var(--text);position:relative;font-size:9px}
.abs{position:absolute}
.brand{left:19px;top:14px;font-size:22px;font-weight:500;color:var(--blue)}
.tabs{left:15px;top:56px;display:flex;align-items:center;height:31px;font-size:8px;font-weight:500;color:var(--ink)}
.tab{padding:0 18px;height:31px;line-height:31px}
.tab.active{background:var(--green);color:#fff;border-radius:4px 4px 0 0;width:125px;text-align:center;padding:0}
.global{color:var(--orange);margin-left:16px}
.global span{color:#666;font-weight:400}
.greet{right:21px;top:41px;display:flex;align-items:center;gap:6px;font-size:8px;color:#666}
.greet b{color:var(--orange);font-size:12px;font-weight:500}
.avatar{border-radius:50%;background:var(--avatar);display:inline-block;flex:none}
.mainnav{left:0;top:87px;width:1103px;height:55px;background:linear-gradient(var(--blue-light),var(--blue-dark));display:flex;justify-content:center;align-items:center;gap:49px;color:#fff;font-size:13px;font-weight:500;padding-right:20px}
.title{left:0;width:1103px;top:175px;text-align:center;font-size:12px;font-weight:500;color:var(--ink)}
.works h3{font-size:9.5px;font-weight:500;color:var(--ink);display:flex;align-items:center;gap:6px;height:20px}
.works{top:222px}
.list{margin-top:12px;border:1px solid var(--line)}
.list .r{height:31.6px;display:flex;align-items:center;padding:0 6px;font-size:8px;border-bottom:1px solid var(--line)}
.list .r:nth-child(odd){background:var(--row)}
.list .r:last-child{border-bottom:none}
.r .f{flex:1}
.r .doc{width:12px;height:13px;margin-right:6px}
.seeall{left:21px;top:438px;width:1060px;height:44px;background:repeating-linear-gradient(45deg,#f3f3f3 0 2px,#ececec 2px 3px);text-align:center;line-height:44px;font-size:12px;font-weight:500;color:var(--blue)}
.mynav{left:21px;top:510px;width:1060px;height:44px;border:1px solid var(--line);display:flex;align-items:center;padding-left:23px;font-size:9.5px;color:#333}
.mynav b{font-weight:500;color:var(--ink);margin-right:4px}
.mynav i{font-style:normal;margin:0 9px;color:#555}
.card{border:1px solid var(--line);box-shadow:0 0 3px rgba(0,0,0,.05)}
.card h2{font-size:12.5px;font-weight:500;color:var(--ink);line-height:16px}
.conv{left:22px;top:578px;width:278px;height:557px;padding:0 15px}
.msg{display:flex;align-items:center;gap:10px;font-size:9.5px;line-height:16.5px;color:#333}
.msg .icon{margin-left:auto}
.box{border:1px solid var(--line);height:58px;font-size:8px;color:#999;padding:8px 10px}
.send{background:var(--green);color:#fff;border-radius:6px;width:54px;height:20px;font-size:9.5px;font-weight:500;text-align:center;line-height:20px;margin-left:auto}
.teams{left:309px;top:578px;width:174px;height:250px;padding:0 14px}
.teams p{font-size:9.5px;color:#333;height:33px}
.news{left:492px;top:578px;width:588px;height:250px;padding:0 17px}
.news .n{display:flex;font-size:9.5px;color:#333;height:43px}
.news .n .t{width:370px;white-space:nowrap;overflow:hidden;text-overflow:ellipsis}
.news .n .h{width:82px;text-align:left}
.coll{left:309px;top:837px;width:174px;height:298px;padding:0 12px}
.person{display:flex;align-items:center;gap:14px;height:51px}
.person b{display:block;font-size:9.5px;font-weight:500;color:var(--ink)}
.person span{font-size:8px;color:#555}
.analytics{left:492px;top:837px;width:588px;height:298px}
.footer{left:0;top:1173px;width:1103px;text-align:center;font-size:9.5px;color:#444}
</style>
</head>
<body>

<div class="abs brand">Corehub</div>

<div class="abs tabs">
  <div class="tab active">Enterprise Homepage</div>
  <div class="tab">Dept. View</div>
  <div class="tab">My View</div>
  <div class="global">Global Nav : <span>Link 1 | &nbsp;Link 2 &nbsp;| &nbsp;Link3</span></div>
</div>

<div class="abs greet">
  <span class="avatar" role="img" aria-label="Profile photo of Jane" style="width:32px;height:32px;margin-top:-22px"></span>
  <span style="margin-top:-6px">Good Morning <b>Jane !</b></span>
</div>

<nav class="abs mainnav">
  <span>My HR</span><span>My Training</span><span>My Benefits</span><span>My Dependents</span><span>My Health Insurance</span><span>My Salary</span>
</nav>

<div class="abs title">MY WORKS</div>

<!-- Recent docs -->
<section class="abs works" style="left:21px;width:232px">
  <h3><svg width="14" height="16" viewBox="0 0 14 16"><path d="M0 0h9l5 5v11H0z" fill="var(--green)"/><path d="M3 8h8M3 11h8M3 13.5h6" stroke="#fff" stroke-width="1.2"/></svg>My Recent Docs</h3>
  <div class="list">
    <div class="r"><svg class="doc" viewBox="0 0 12 13"><rect x=".5" y=".5" width="11" height="12" fill="none" stroke="#333"/><text x="2" y="10" font-size="8" font-family="Arial" fill="#333">W</text></svg><span class="f">Neque porro quisquam est qui</span>4-7-2017</div>
    <div class="r"><svg class="doc" viewBox="0 0 12 13"><path d="M.5.5h8l3 3v9H.5z" fill="none" stroke="#333"/><path d="M3 9l3-5 3 5z" fill="none" stroke="#333"/></svg><span class="f">Dolorem ipsum quia dolor sit</span>4-7-2017</div>
    <div class="r"><svg class="doc" viewBox="0 0 12 13"><path d="M.5.5h8l3 3v9H.5z" fill="none" stroke="#333"/><path d="M3 5l5 5M8 5l-5 5" stroke="#333"/></svg><span class="f">Sed ut perspiciatis unde omnis iste</span>4-7-2017</div>
    <div class="r"><svg class="doc" viewBox="0 0 12 13"><rect x=".5" y=".5" width="11" height="12" fill="none" stroke="#333"/><text x="2" y="10" font-size="8" font-family="Arial" fill="#333">W</text></svg><span class="f">Porro quisquam est qui</span>4-7-2017</div>
    <div class="r"><svg class="doc" viewBox="0 0 12 13"><rect x=".5" y=".5" width="11" height="12" fill="none" stroke="#333"/><text x="2" y="10" font-size="8" font-family="Arial" fill="#333">W</text></svg><span class="f">Quisquam est qui</span>4-7-2017</div>
  </div>
</section>

<!-- Recent emails -->
<section class="abs works" style="left:266px;width:326px">
  <h3><svg width="16" height="12" viewBox="0 0 16 12"><rect x=".75" y=".75" width="14.5" height="10.5" fill="none" stroke="var(--green)" stroke-width="1.5"/><path d="M1 1l7 6 7-6" fill="none" stroke="var(--green)" stroke-width="1.5"/></svg>My Recent Emails</h3>
  <div class="list">
    <div class="r"><span class="f" style="flex:0 0 159px">Neque porro quisquam est qui</span><span class="f">Robert Jones</span>09:50 AM</div>
    <div class="r"><span class="f" style="flex:0 0 159px">Dolorem ipsum quia dolor sit</span><span class="f">Micheal Clarke</span>10:15 AM</div>
    <div class="r"><span class="f" style="flex:0 0 159px">Sed ut perspiciatis unde omnis iste</span><span class="f">Ian Tins</span>11:15 AM</div>
    <div class="r"><span class="f" style="flex:0 0 159px">Porro quisquam est qui</span><span class="f">Jenifer Mollis</span>12:15 PM</div>
    <div class="r"><span class="f" style="flex:0 0 159px">Quisquam est qui</span><span class="f">Meetin Jacks</span>01:15 PM</div>
  </div>
</section>

<!-- Meetings -->
<section class="abs works" style="left:605px;width:232px">
  <h3><svg width="14" height="14" viewBox="0 0 14 14"><circle cx="7" cy="7" r="6" fill="none" stroke="var(--green)" stroke-width="1.6"/><path d="M7 3.5V7H4.5" fill="none" stroke="var(--green)" stroke-width="1.4"/></svg>My Upcoming Meetings</h3>
  <div class="list">
    <div class="r"><span style="width:79px">Meeting 1</span><span class="f">HQ2 7B-073</span>09:50 AM</div>
    <div class="r"><span style="width:79px">Meeting 2</span><span class="f">HQ2 7B-073</span>10:15 AM</div>
    <div class="r"><span style="width:79px">Meeting 3</span><span class="f">HQ2 7B-073</span>11:15 AM</div>
    <div class="r"><span style="width:79px">Meeting 4</span><span class="f">HQ2 7B-073</span>12:15 PM</div>
    <div class="r"><span style="width:79px">Meeting 5</span><span class="f">HQ2 7B-073</span>01:15 PM</div>
  </div>
</section>

<!-- Tasks -->
<section class="abs works" style="left:850px;width:231px">
  <h3><svg width="16" height="14" viewBox="0 0 16 14"><path d="M1 4h4V2a2 2 0 014 0v2h4v4h2a2 2 0 010 4h-2v2H1z" fill="var(--green)"/></svg>My Tasks</h3>
  <div class="list">
    <div class="r"><span class="f">Review Georgia's 2017 Article IV Report</span>4-7-2017</div>
    <div class="r"><span class="f">Submit Conference Selections</span>4-7-2017</div>
    <div class="r"><span class="f">Complete GSRR chapter 2 data analysis</span>4-7-2017</div>
    <div class="r"></div>
    <div class="r"></div>
  </div>
</section>

<div class="abs seeall">SEE ALL</div>

<div class="abs mynav"><b>My Navigation :</b>Create New Document<i>|</i>Create New Spreadsheet<i>|</i>Create New Email message<i>|</i>Schedule a meeting<i>|</i>Create New Task<i>|</i>Book Travel<i>|</i>Submit Expenses</div>

<!-- Conversations -->
<section class="abs card conv">
  <h2 style="display:flex;align-items:center;gap:10px;margin:20px 0 0 5px"><svg width="18" height="15" viewBox="0 0 18 15"><ellipse cx="7" cy="6" rx="6" ry="4.5" fill="none" stroke="var(--green)" stroke-width="1.5"/><path d="M3 10l-1 3 4-2" fill="var(--green)"/><path d="M13 4.5c2.5.8 4 2.5 3.5 4.5l.8 3-3-1.5c-2 .8-4.5.3-6-1" fill="none" stroke="var(--green)" stroke-width="1.5"/></svg>My Recent Conversations</h2>
  <div class="msg" style="margin-top:22px"><span class="avatar" role="img" aria-label="Colleague photo" style="width:34px;height:34px"></span><span>Sed ut perspiciatis unde omnis iste<br>natus error sit voluptatem</span><svg class="icon" width="10" height="10" viewBox="0 0 10 10"><path d="M1 4h2v5.5H1zM3 4l2-3.5c1 0 1.2.7 1 1.6L5.6 4H9l-.8 5.5H3" fill="none" stroke="#222" stroke-width=".9"/></svg></div>
  <div class="msg" style="margin-top:24px"><span class="avatar" role="img" aria-label="Colleague photo" style="width:34px;height:34px"></span><span>Sed ut perspiciatis unde omnis iste<br>natus error sit voluptatem</span><svg class="icon" width="11" height="10" viewBox="0 0 11 10"><path d="M5.5 9.5L1 5a2.6 2.6 0 014.5-3 2.6 2.6 0 014.5 3z" fill="var(--orange)"/></svg></div>
  <div class="box" style="margin-top:15px">Type your Message</div>
  <div class="send" style="margin-top:8px">Send</div>
  <div class="msg" style="margin-top:54px"><span class="avatar" role="img" aria-label="Colleague photo" style="width:34px;height:34px"></span><span>Sed ut perspiciatis unde omnis iste<br>natus error sit voluptatem</span><svg class="icon" width="10" height="10" viewBox="0 0 10 10"><path d="M1 4h2v5.5H1zM3 4l2-3.5c1 0 1.2.7 1 1.6L5.6 4H9l-.8 5.5H3" fill="none" stroke="#222" stroke-width=".9"/></svg></div>
  <div class="msg" style="margin-top:24px"><span class="avatar" role="img" aria-label="Colleague photo" style="width:34px;height:34px"></span><span>Sed ut perspiciatis unde omnis iste<br>natus error sit voluptatem</span><svg class="icon" width="11" height="10" viewBox="0 0 11 10"><path d="M5.5 9.5L1 5a2.6 2.6 0 014.5-3 2.6 2.6 0 014.5 3z" fill="var(--orange)"/></svg></div>
  <div class="box" style="margin-top:15px">Type your Message</div>
  <div class="send" style="margin-top:8px">Send</div>
</section>

<!-- Teams -->
<section class="abs card teams">
  <div style="display:flex;gap:12px;margin-top:20px"><svg width="20" height="16" viewBox="0 0 20 16" style="margin-top:2px"><circle cx="10" cy="4" r="3" fill="var(--green)"/><circle cx="4" cy="6" r="2.3" fill="var(--green)"/><circle cx="16" cy="6" r="2.3" fill="var(--green)"/><path d="M5 15a5 5 0 0110 0z M0 14a4 4 0 017 0z M13 14a4 4 0 017 0z" fill="var(--green)"/></svg><h2>My Teams/<br>Communities</h2></div>
  <div style="margin-top:16px">
    <p>Bulgaria - June 2017 Mission</p>
    <p>Romania - April 2016 Mission</p>
    <p>Bulgaria Country Team</p>
    <p>Macedonia Country Team</p>
  </div>
  <div style="text-align:right;margin-top:23px;margin-right:14px;font-size:9.5px;font-weight:500;color:var(--blue);text-decoration:underline">See All</div>
</section>

<!-- News -->
<section class="abs card news">
  <h2 style="display:flex;align-items:center;gap:12px;margin:21px 0 0 0"><svg width="16" height="17" viewBox="0 0 16 17"><path d="M1 1h8l3 3v12H1z" fill="none" stroke="var(--green)" stroke-width="1.6"/><path d="M5 5h9v11H5z" fill="var(--green)"/></svg>My News Report</h2>
  <div style="margin-top:28px">
    <div class="n"><span class="t">Banks' Preparations for Brexit Need to Improve - CMB, NRB (Newswire)</span><span class="h">11:32 am</span><span>4-7-2017</span></div>
    <div class="n"><span class="t">Eurozone recovery broadening but gaps remain (GPA)</span><span class="h">11:32 am</span><span>6-7-2017</span></div>
    <div class="n"><span class="t">Lorem ipsum dolor sit amet, et donec ligula feugiat, tempor quis consectetur</span><span class="h">11:32 am</span><span>9-7-2017</span></div>
  </div>
</section>

<!-- Colleagues -->
<section class="abs card coll">
  <div style="display:flex;gap:14px;margin-top:20px"><svg width="14" height="16" viewBox="0 0 14 16" style="margin-top:4px"><circle cx="7" cy="4.5" r="3.8" fill="var(--green)"/><path d="M0 16a7 6 0 0114 0z" fill="var(--green)"/></svg><h2>My Colleagues /<br>Frequent Contacts</h2></div>
  <div style="margin-top:14px">
    <div class="person"><span class="avatar" role="img" aria-label="Photo of Robert Thomas" style="width:35px;height:35px"></span><div><b>Robert Thomas</b><span>Mission Chief</span></div></div>
    <div class="person"><span class="avatar" role="img" aria-label="Photo of Chang Lee" style="width:35px;height:35px"></span><div><b>Chang Lee</b><span>Senior Economist</span></div></div>
    <div class="person"><span class="avatar" role="img" aria-label="Photo of Oswald Muhoza" style="width:35px;height:35px"></span><div><b>Oswald Muhoza</b><span>Resident Rep</span></div></div>
    <div class="person"><span class="avatar" role="img" aria-label="Photo of Jurgen Klaus" style="width:35px;height:35px"></span><div><b>Jurgen Klaus</b><span>Desk Economist</span></div></div>
  </div>
</section>

<!-- Analytics -->
<section class="abs card analytics">
  <svg width="588" height="298" viewBox="0 0 588 298" font-family="Rubik, Arial, sans-serif">
    <g transform="translate(17,30)"><path d="M8 0A8 8 0 108 16 8 8 0 008 8z" fill="var(--green)"/><path d="M10 -1a8 8 0 018 8h-8z" fill="var(--green)"/></g>
    <text x="54" y="43" font-size="12.5" font-weight="500" fill="#1d1d1d">My Analytics</text>
    <!-- bar chart -->
    <g font-size="8" fill="#444">
      <g stroke="#e2e2e2" stroke-width=".8">
        <line x1="40" x2="190" y1="88" y2="88"/><line x1="40" x2="190" y1="119" y2="119"/><line x1="40" x2="190" y1="149" y2="149"/><line x1="40" x2="190" y1="180" y2="180"/><line x1="40" x2="190" y1="211" y2="211"/><line x1="40" x2="190" y1="242" y2="242"/>
      </g>
      <text x="15" y="91">250</text><text x="15" y="122">200</text><text x="15" y="152">150</text><text x="15" y="183">100</text><text x="18" y="214">50</text><text x="20" y="245">0</text>
      <g fill="var(--blue)">
        <rect x="39" y="211" width="7" height="31"/><rect x="54" y="180" width="7" height="62"/><rect x="68" y="149" width="7" height="93"/><rect x="83" y="119" width="7" height="123"/>
        <rect x="97" y="88" width="7" height="154" fill="var(--orange)"/>
        <rect x="112" y="119" width="7" height="123"/><rect x="126" y="119" width="7" height="123"/><rect x="141" y="149" width="7" height="93"/><rect x="155" y="180" width="7" height="62"/><rect x="170" y="149" width="7" height="93"/>
      </g>
      <g font-size="5" fill="#555" text-anchor="middle">
        <text x="42" y="252">Jan</text><text x="57" y="252">Jan</text><text x="71" y="252">Jan</text><text x="86" y="252">Jan</text><text x="100" y="252">Jan</text><text x="115" y="252">Jan</text><text x="129" y="252">Jan</text><text x="144" y="252">Jan</text><text x="158" y="252">Jan</text><text x="173" y="252">Jan</text>
      </g>
      <g font-size="4" fill="#aaa" text-anchor="middle">
        <text x="42" y="258">01</text><text x="57" y="258">02</text><text x="71" y="258">04</text><text x="86" y="258">05</text><text x="100" y="258">06</text><text x="115" y="258">07</text><text x="129" y="258">08</text><text x="144" y="258">09</text><text x="158" y="258">10</text><text x="173" y="258">11</text>
      </g>
    </g>
    <!-- donut -->
    <g transform="translate(279,163) rotate(-90)" fill="none" stroke-width="5">
      <circle r="50" stroke="#cfcfcf"/>
      <circle r="50" stroke="var(--blue)" stroke-dasharray="160 314" stroke-dashoffset="-65"/>
      <circle r="50" stroke="var(--orange)" stroke-dasharray="50 314" stroke-dashoffset="-225"/>
      <circle r="50" stroke="var(--green)" stroke-dasharray="40 314" stroke-dashoffset="-275"/>
    </g>
    <text x="279" y="166" font-size="13" font-weight="500" fill="var(--blue)" text-anchor="middle">Corehub</text>
    <text x="279" y="180" font-size="7" font-weight="500" fill="#222" text-anchor="middle">My Analytics</text>
    <!-- line chart -->
    <g font-size="8" fill="#444">
      <g stroke="#e2e2e2" stroke-width=".8">
        <line x1="370" x2="568" y1="88" y2="88"/><line x1="370" x2="568" y1="119" y2="119"/><line x1="370" x2="568" y1="149" y2="149"/><line x1="370" x2="568" y1="180" y2="180"/><line x1="370" x2="568" y1="211" y2="211"/><line x1="370" x2="568" y1="242" y2="242"/>
      </g>
      <text x="347" y="91">250</text><text x="347" y="122">200</text><text x="347" y="152">150</text><text x="347" y="183">100</text><text x="350" y="214">50</text><text x="352" y="245">0</text>
      <polyline points="372,237 404,213 441,190 485,206 534,164 574,136" fill="none" stroke="var(--blue)" stroke-width="1"/>
      <polyline points="374,201 400,221 416,201 453,211 489,190 525,199 567,132" fill="none" stroke="var(--green)" stroke-width="1"/>
      <g font-size="5" fill="#555" text-anchor="middle">
        <text x="376" y="252">Jan</text><text x="397" y="252">Jan</text><text x="418" y="252">Jan</text><text x="439" y="252">Jan</text><text x="460" y="252">Jan</text><text x="481" y="252">Jan</text><text x="502" y="252">Jan</text><text x="523" y="252">Jan</text><text x="544" y="252">Jan</text><text x="565" y="252">Jan</text>
      </g>
      <g font-size="4" fill="#aaa" text-anchor="middle">
        <text x="376" y="258">01</text><text x="397" y="258">02</text><text x="418" y="258">04</text><text x="439" y="258">05</text><text x="460" y="258">06</text><text x="481" y="258">07</text><text x="502" y="258">08</text><text x="523" y="258">09</text><text x="544" y="258">10</text><text x="565" y="258">11</text>
      </g>
    </g>
  </svg>
</section>

<div class="abs footer">© 2017 Company Name &nbsp;| &nbsp;All Rights Reserved</div>

</body>
</html>
```